Trucking company specializing in intermodal containers

We need a logo design for our trucking company based in Kent, Washington. Our companies name is Dorvale Haulworks LLC, we specialize in intermodal containers, and work off of the Crestmark rail lines and the ports. We provide service by transporting freight with our fleet of trucks. We operate within Washington, Oregon, and Idaho. Our fleet consists of an east division and a local division. Our team motto currently is globally connected, locally invested.

Target Market(s)

brokers, intermodal management companies, customers

Industry/Entity Type

Trucking Company

Contact Information for Business Card

physical address 4519 N. 163rd Pl Kent, WA 98517
office number is 253-614-9026

Font styles to use
Sans Serif

Colors

Designer to choose colors to be used in the design.

Requirements
Must have
• We need to update our current logo. Something like an emblem; that makes a statement that this logo/ sign represents Dorvale Haulworks. Something like a royal stamp but in this case a royal shield.
Nice to have
• simple, yet bold. something someone does not currently have. We need something fresh and exciting. Something that will also make a statement because currently our reputation is great within the industry and our community. But we need to reflect that we are professional and willing to provide the best service. We are open to new statement lines.
Should not have
• Should not have something thats been used before. We are open to suggestions that you have and a design that is completely unique and you make originally without what we want but what you like as well. Ofcourse it should still represent the industry we are in.

```html
<!DOCTYPE html>
<html lang="en">
<head>
<meta charset="utf-8">
<title>Dorvale Haulworks LLC – Business Card</title>
<link rel="stylesheet" href="https://fonts.googleapis.com/css2?family=Open+Sans:wght@400;600;700&display=swap">
<style>
  :root {
    --canvas: #e9eaec;
    --card-white: #ffffff;
    --sand: #e8e0cf;
    --royal-blue: #0a6bb8;
    --sky-blue: #3aa9e0;
    --ink: #1e1e1e;
    --shadow: rgba(0, 0, 0, 0.18);
  }
  * { box-sizing: border-box; margin: 0; padding: 0; }
  html, body {
    width: 1200px;
    height: 1006px;
    overflow: hidden;
    background: var(--canvas);
    font-family: "Open Sans", Arial, sans-serif;
  }
  .sheet {
    position: relative;
    width: 1200px;
    height: 1006px;
  }
  .card {
    position: absolute;
    left: 215px;
    width: 770px;
    height: 440px;
    background: var(--card-white);
    box-shadow: 0 10px 28px var(--shadow);
    overflow: hidden;
  }
  .card--front { top: 48px; }
  .card--back  { top: 518px; }
  .card__shapes {
    position: absolute;
    inset: 0;
    width: 100%;
    height: 100%;
  }
  .brand-mark {
    position: absolute;
    display: flex;
    align-items: center;
    gap: 12px;
    color: var(--sky-blue);
    font-weight: 700;
    white-space: nowrap;
  }
  .brand-mark__dot {
    width: 18px;
    height: 18px;
    border-radius: 50%;
    background: var(--sky-blue);
    flex: none;
  }
  .card--front .brand-mark {
    left: 360px;
    top: 108px;
    font-size: 30px;
  }
  .card--back .brand-mark {
    right: 26px;
    bottom: 56px;
    font-size: 16px;
    gap: 8px;
  }
  .card--back .brand-mark__dot { width: 12px; height: 12px; }
  .company-name {
    position: absolute;
    left: 150px;
    top: 92px;
    font-size: 24px;
    font-weight: 600;
    color: var(--ink);
  }
  .contact-list {
    position: absolute;
    left: 50px;
    top: 200px;
    list-style: none;
    display: flex;
    flex-direction: column;
    gap: 26px;
    font-size: 15px;
    color: var(--ink);
  }
  .contact-list__item {
    display: flex;
    align-items: center;
    gap: 16px;
  }
  .contact-list__icon {
    width: 16px;
    height: 18px;
    flex: none;
    fill: var(--royal-blue);
  }
</style>
</head>
<body>
<main class="sheet">

  <!-- Front of card -->
  <section class="card card--front" aria-label="Business card front">
    <svg class="card__shapes" viewBox="0 0 770 440" aria-hidden="true">
      <polygon points="0,250 0,440 330,440" fill="var(--sand)"/>
      <polygon points="0,180 0,250 330,440 430,440" fill="var(--royal-blue)"/>
      <polygon points="40,150 150,150 250,220 140,220" fill="var(--sky-blue)"/>
      <polygon points="560,440 770,320 770,440" fill="var(--royal-blue)"/>
    </svg>
    <div class="brand-mark">
      <span class="brand-mark__dot"></span>
      <span class="brand-mark__name">Dorvale Haulworks LLC</span>
    </div>
  </section>

  <!-- Back of card -->
  <section class="card card--back" aria-label="Business card back">
    <svg class="card__shapes" viewBox="0 0 770 440" aria-hidden="true">
      <polygon points="0,0 625,0 440,360 0,360" fill="var(--sand)"/>
      <polygon points="0,0 70,0 0,40" fill="var(--royal-blue)"/>
      <polygon points="0,360 440,360 400,440 0,440" fill="var(--royal-blue)"/>
      <polygon points="625,0 715,0 490,440 400,440" fill="var(--royal-blue)"/>
      <polygon points="0,110 120,55 70,150 0,180" fill="var(--sky-blue)"/>
      <polygon points="725,25 770,25 770,80 710,190 645,190" fill="var(--sky-blue)"/>
    </svg>

    <h1 class="company-name">Dorvale Haulworks LLC.</h1>

    <ul class="contact-list">
      <li class="contact-list__item">
        <svg class="contact-list__icon" viewBox="0 0 16 18" aria-label="Phone" role="img">
          <path d="M3 1 L6 1 L7 5 L5 6.5 C6 9.5 7.5 11.5 10 13 L11.5 11 L15 12.5 L15 16 C15 17 14 17.5 13 17.3 C7 16 2 10.5 1.5 3.5 C1.5 2 2 1 3 1 Z"/>
        </svg>
        <span>253-614-9026</span>
      </li>
      <li class="contact-list__item">
        <svg class="contact-list__icon" viewBox="0 0 16 18" aria-label="Address" role="img">
          <path d="M8 0 C3.8 0 1 3 1 6.6 C1 11 8 18 8 18 C8 18 15 11 15 6.6 C15 3 12.2 0 8 0 Z M8 9.4 C6.4 9.4 5.2 8.2 5.2 6.6 C5.2 5 6.4 3.8 8 3.8 C9.6 3.8 10.8 5 10.8 6.6 C10.8 8.2 9.6 9.4 8 9.4 Z"/>
        </svg>
        <span>4519 N. 163rd Pl Kent, WA 98517</span>
      </li>
    </ul>

    <div class="brand-mark">
      <span class="brand-mark__dot"></span>
      <span class="brand-mark__name">Dorvale Haulworks LLC</span>
    </div>
  </section>

</main>
</body>
</html>
```